for an application under development,
this application will be used for the management of files in a company for several remote collaborators.
it is like an internal messaging system where files will be opened for such and such a person or group of people.

Target Market(s)

business

Number of Pages Required

5+ page

Requirements
Nice to have
• a visual with the view of a connection between computer and / or smart phones
the name of my application; "LumaKTrovenar"

```html
<!DOCTYPE html>
<html lang="en">
<head>
<meta charset="utf-8">
<title>LumaKTrovenar</title>
<link href="https://fonts.googleapis.com/css2?family=Bitter:wght@600;700&family=Montserrat:wght@400;500;600;700&display=swap" rel="stylesheet">
<style>
:root{
  --blue:#0a70b6;
  --blue-dark:#0457a0;
  --blue-light:#0b98d6;
  --purple:#66287a;
  --ink:#2e2e2e;
  --muted:#777;
  --line:#e6e9ee;
  --white:#fff;
}
*{margin:0;padding:0;box-sizing:border-box}
html,body{width:1200px;height:3763px;overflow:hidden;background:var(--white)}
body{font-family:'Montserrat',sans-serif;color:var(--ink)}
.page{position:relative;width:1200px;height:3763px;overflow:hidden}
.abs{position:absolute}

/* hero */
.hero-visual{left:0;top:0;width:1200px;height:720px;
  background:radial-gradient(ellipse at 60% 45%,#c98a6a 0%,#4a5f92 28%,#1d3f86 55%,#0f2a66 100%)}
.hero-shade{left:0;top:0;width:1200px;height:720px;background:linear-gradient(180deg,rgba(10,30,80,.35),rgba(10,30,80,.15))}
.top-bar{left:0;top:0;width:1200px;height:4px;background:var(--blue)}
.brand{left:143px;top:46px;font-family:'Bitter',serif;font-weight:700;font-size:33px;color:var(--blue);letter-spacing:.3px}
.nav{left:482px;top:56px;display:flex;gap:23px;font-size:14.5px;font-weight:500;color:var(--white)}
.nav a{color:var(--white);text-decoration:none;position:relative}
.nav a.active{color:#e8eef7}
.nav a.active::after{content:"";position:absolute;left:0;right:0;top:24px;height:2px;background:var(--white)}
.hero-title{left:230px;top:246px;width:740px;text-align:center;font-family:'Bitter',serif;font-weight:700;font-size:42px;line-height:52px;color:var(--white);text-transform:uppercase}
.btn{display:inline-flex;align-items:center;justify-content:center;gap:9px;border-radius:27px;color:var(--white);font-weight:700;font-size:14px;text-transform:uppercase;letter-spacing:.2px}
.btn .arr{width:13px;height:13px}
.btn-blue{background:var(--blue)}
.btn-purple{background:var(--purple)}
.hero-btn{left:505px;top:427px;width:190px;height:52px}
.dots{left:1134px;top:283px;display:flex;flex-direction:column;gap:8px}
.dots i{width:10px;height:10px;border-radius:50%;background:var(--white);display:block}
.dots i.on{background:transparent;border:2px solid var(--white)}
.hero-wave{left:0;top:560px}

/* features */
.feature{width:300px;text-align:center}
.feature h3{font-size:20px;font-weight:500;letter-spacing:.4px;color:#222}
.feature p{margin-top:22px;font-size:12.5px;line-height:24px;color:var(--muted)}

/* about */
.about-bg{left:0;top:921px}
.about-screen{left:70px;top:1090px;width:500px;height:550px;border-radius:24px;
  background:linear-gradient(160deg,#f4f6fa 0%,#dde3ee 55%,#c8d1e2 100%)}
.about-title{left:615px;top:1114px;font-family:'Bitter',serif;font-weight:700;font-size:42px;color:var(--white)}
.about-rule{left:617px;top:1184px;width:47px;height:4px;background:var(--white)}
.about-text{left:616px;top:1218px;width:420px;font-size:13.5px;line-height:27.3px;color:var(--white)}
.about-btn{left:616px;top:1412px;width:190px;height:52px}

/* news */
.section-title{left:0;width:1200px;text-align:center;font-family:'Bitter',serif;font-weight:700;font-size:42px;color:#333}
.section-title span{color:var(--purple)}
.section-rule{left:576px;width:48px;height:4px;background:var(--blue);border-radius:2px}
.card{background:var(--white);border:1px solid #eef0f4;border-radius:22px;box-shadow:0 2px 10px rgba(0,0,0,.04);overflow:hidden}
.card-photo{border-radius:22px}
.date{font-size:13px;color:var(--blue);font-weight:500}
.card h4{font-size:19px;line-height:25px;font-weight:500;color:#222}
.card p{font-size:10.5px;line-height:25px;color:#999}
.more{font-size:15px;font-weight:700;color:var(--purple);letter-spacing:.3px}
.card-side .body{position:absolute;left:269px;top:30px;width:310px}
.card-side .body h4{margin-top:18px}
.card-side .body p{margin-top:10px}
.card-side .body .more{margin-top:10px}

/* contact */
.touch-bg{left:0;top:2485px}
.field{background:var(--white);border:1px solid #e4e8ee;font-size:14px;color:#444;padding:16px 21px}
.submit-btn{left:493px;top:3089px;width:215px;height:52px}
.info{width:250px;text-align:center}
.ring{width:72px;height:72px;border-radius:50%;border:2px solid #9aa5b4;margin:0 auto;display:flex;align-items:center;justify-content:center}
.ring.fill{background:var(--blue);border-color:var(--blue)}
.info h5{margin-top:26px;font-size:15px;font-weight:700;color:#222;letter-spacing:.3px}
.info p{margin-top:6px;font-size:12.5px;line-height:21px;color:var(--muted)}
.foot-line{top:3638px;height:1px;background:var(--line)}
.social{top:3618px;width:41px;height:41px;border-radius:50%;border:1.5px solid #555;display:flex;align-items:center;justify-content:center;background:var(--white)}
.social i{width:9px;height:9px;border-radius:50%;background:var(--purple);display:block}
.copyright{left:0;top:3700px;width:1200px;text-align:center;font-size:12.5px;color:#666}
.bottom-bar{left:0;top:3759px;width:1200px;height:4px;background:var(--blue)}
</style>
</head>
<body>
<div class="page">

  <!-- hero -->
  <div class="abs hero-visual" role="img" aria-label="Photo of hands typing on a laptop with code and binary digits overlaid"></div>
  <div class="abs hero-shade"></div>
  <div class="abs top-bar"></div>
  <div class="abs brand">LUMAKTROVENAR</div>
  <nav class="abs nav">
    <a class="active">HOME</a><a>ABOUT US</a><a>SERVICES</a><a>COLLABORATORS</a><a>NEWS</a><a>CONTACT</a>
  </nav>
  <h1 class="abs hero-title">A visual with the view of a<br>connection between computer<br>or smart phones</h1>
  <div class="abs btn btn-blue hero-btn">Get started
    <svg class="arr" viewBox="0 0 14 14"><circle cx="7" cy="7" r="7" fill="#fff"/><path d="M5 4l3.5 3L5 10" stroke="#0a70b6" stroke-width="2" fill="none"/></svg></div>
  <div class="abs dots"><i></i><i></i><i class="on"></i><i></i><i></i></div>

  <svg class="abs hero-wave" width="1200" height="170" viewBox="0 0 1200 170">
    <path d="M0 20 C40 10 70 40 110 70 C150 100 200 110 250 90 C300 75 330 80 360 80 L520 80 C560 80 570 110 600 115 C640 118 650 80 690 80 L840 80 C890 82 950 120 990 110 C1040 98 1080 60 1130 40 C1160 28 1185 10 1200 5 L1200 170 L0 170 Z" fill="#0a70b6"/>
    <path d="M0 36 C40 30 70 60 110 85 C150 110 200 122 250 105 C300 90 330 98 360 98 L520 98 C560 98 570 125 600 128 C640 130 650 98 690 98 L840 98 C890 100 950 132 990 124 C1040 112 1080 78 1130 58 C1160 46 1185 30 1200 24 L1200 170 L0 170 Z" fill="#fff"/>
    <circle cx="221" cy="83" r="70" fill="#0a70b6"/><circle cx="221" cy="83" r="56" fill="#fff"/>
    <circle cx="601" cy="83" r="70" fill="#66287a"/><circle cx="601" cy="83" r="56" fill="#fff"/>
    <circle cx="982" cy="83" r="70" fill="#0a70b6"/><circle cx="982" cy="83" r="56" fill="#fff"/>
    <g fill="none" stroke="#222" stroke-width="2">
      <circle cx="221" cy="68" r="10"/><path d="M198 100 l14 -14 h18 l14 14 M205 92 l10 10 M213 88 l10 10"/>
      <rect x="578" y="58" width="22" height="14" rx="3"/><rect x="604" y="64" width="22" height="16" rx="3"/><circle cx="593" cy="94" r="10"/><circle cx="593" cy="94" r="4"/><circle cx="614" cy="98" r="6"/>
      <circle cx="982" cy="60" r="8"/><path d="M982 68 v10 M970 86 l12 -8 l12 8"/><circle cx="966" cy="92" r="5"/><circle cx="982" cy="92" r="5"/><circle cx="998" cy="92" r="5"/><path d="M958 108 q8 -10 16 0 M974 108 q8 -10 16 0 M990 108 q8 -10 16 0"/>
    </g>
  </svg>

  <div class="abs feature" style="left:71px;top:741px"><h3>VOLUPTATEM</h3><p>Lorem ipsum dolor sit amet, consectetur adipiscing elit, sed do eiusmod tempor incididunt ut laboe magna aliqua</p></div>
  <div class="abs feature" style="left:451px;top:741px"><h3>COMMODO</h3><p>Lorem ipsum dolor sit amet, consectetur adipiscing elit, sed do eiusmod tempor incididunt ut laboe magna aliqua</p></div>
  <div class="abs feature" style="left:832px;top:741px"><h3>DUIS AUTE</h3><p>Lorem ipsum dolor sit amet, consectetur adipiscing elit, sed do eiusmod tempor incididunt ut laboe magna aliqua</p></div>

  <!-- about -->
  <svg class="abs about-bg" width="1200" height="720" viewBox="0 0 1200 720">
    <defs><linearGradient id="aboutGrad" x1="0" y1="0" x2="0" y2="1"><stop offset="0" stop-color="#0b98d6"/><stop offset="1" stop-color="#0457a0"/></linearGradient></defs>
    <path d="M0 130 C40 100 60 60 110 45 C170 28 220 55 280 40 C340 25 380 -10 450 5 C520 20 550 110 620 110 C690 110 710 5 800 2 C900 0 940 60 1000 70 C1070 80 1100 40 1140 60 C1170 75 1185 110 1200 130 L1200 570 C1160 560 1120 590 1090 600 C1040 620 1000 580 950 570 C880 555 820 600 760 640 C700 680 640 720 560 710 C480 700 460 620 400 600 C330 580 280 650 220 640 C150 628 120 560 60 550 C30 545 10 560 0 570 Z" fill="url(#aboutGrad)"/>
  </svg>
  <div class="abs about-screen" role="img" aria-label="Desktop monitor showing a file management dashboard"></div>
  <h2 class="abs about-title">ABOUT LUMAKTROVENAR</h2>
  <div class="abs about-rule"></div>
  <p class="abs about-text">Lorem ipsum dolor sit amet, consectetur adipiscing elit, sed do eiusmod tempor incididunt ut labore et dolore magna aliquauis ipsum suspendisse ultrices gravidaorem ipsum dolor sit amet, consectetur adipiscing elit, sed do eiusmod tempor incididunt ut labore et dolore magna aliis ipsum suspendisse ultrices gravida</p>
  <div class="abs btn btn-purple about-btn">Get started
    <svg class="arr" viewBox="0 0 14 14"><circle cx="7" cy="7" r="7" fill="#fff"/><path d="M5 4l3.5 3L5 10" stroke="#66287a" stroke-width="2" fill="none"/></svg></div>

  <!-- news -->
  <h2 class="abs section-title" style="top:1725px">LATEST <span>NEWS</span></h2>
  <div class="abs section-rule" style="top:1796px"></div>

  <article class="abs card" style="left:142px;top:1863px;width:296px;height:506px">
    <div class="card-photo" role="img" aria-label="Team joining hands over a desk with business icons" style="width:294px;height:224px;background:linear-gradient(135deg,#c7886a,#7b5a4e 50%,#a9b3c2)"></div>
    <div style="padding:20px 21px 0">
      <div class="date">March.2020</div>
      <h4 style="margin-top:18px">Sed ut perspiciatis unde omnis iste natus</h4>
      <p style="margin-top:14px">Ut enim ad minima veniam, quis nostreierci tationem ullam corporis suscipit laboriosan isi ut aliquid ex ea commodi eprehenderitq ui in ea voluptate velit .</p>
      <div class="more" style="margin-top:10px">READ MORE</div>
    </div>
  </article>

  <article class="abs card card-side" style="left:456px;top:1863px;width:604px;height:246px">
    <div class="card-photo" role="img" aria-label="Person at a laptop with chart and gear icons" style="position:absolute;left:0;top:0;width:237px;height:244px;background:linear-gradient(135deg,#5e6f83,#2c3a4c 60%,#8a97a8)"></div>
    <div class="body"><div class="date">March.2020</div><h4>Sed ut perspiciatis unde omnis iste natus error</h4><p>Ut enim ad minima veniam, quis nostreierci tationem ullam corporis suscipit laboriosan isi ut aliquid ex ea eprehenderitq uiate velit .</p><div class="more">READ MORE</div></div>
  </article>

  <article class="abs card card-side" style="left:456px;top:2125px;width:604px;height:246px">
    <div class="card-photo" role="img" aria-label="Hands working on a laptop with analytics charts overlaid" style="position:absolute;left:0;top:0;width:237px;height:244px;background:linear-gradient(135deg,#3c4b5e,#c98a5c 60%,#34475e)"></div>
    <div class="body"><div class="date">March.2020</div><h4>Sed ut perspiciatis unde omnis iste natus error</h4><p>Ut enim ad minima veniam, quis nostreierci tationem ullam corporis suscipit laboriosan isi ut aliquid ex ea eprehenderitq uiate velit .</p><div class="more">READ MORE</div></div>
  </article>

  <!-- contact -->
  <svg class="abs touch-bg" width="1200" height="870" viewBox="0 0 1200 870">
    <defs><linearGradient id="mistGrad" x1="0" y1="0" x2="0" y2="1"><stop offset="0" stop-color="#f3f6fa"/><stop offset="1" stop-color="#dfe5ee"/></linearGradient></defs>
    <path d="M0 130 C50 90 90 40 150 40 C220 40 250 100 320 80 C390 60 420 20 500 25 C580 30 620 100 690 95 C760 90 790 0 860 5 C940 10 980 80 1050 80 C1110 80 1150 40 1200 60 L1200 740 C1160 760 1130 800 1080 810 C1010 825 960 780 900 780 C820 780 790 850 720 860 C650 870 620 790 560 780 C480 765 440 840 360 845 C280 850 240 780 170 770 C100 760 50 800 0 790 Z" fill="url(#mistGrad)"/>
  </svg>
  <h2 class="abs section-title" style="top:2670px">GET <span>IN TOUCH</span></h2>
  <div class="abs section-rule" style="top:2741px"></div>

  <div class="abs field" style="left:234px;top:2802px;width:358px;height:51px">First Name</div>
  <div class="abs field" style="left:605px;top:2802px;width:360px;height:51px">Last Name</div>
  <div class="abs field" style="left:234px;top:2866px;width:358px;height:51px">Email address</div>
  <div class="abs field" style="left:605px;top:2866px;width:360px;height:51px">Phone Number</div>
  <div class="abs field" style="left:234px;top:2930px;width:731px;height:115px">Message</div>
  <div class="abs btn btn-purple submit-btn">Submit message
    <svg class="arr" viewBox="0 0 14 14"><circle cx="7" cy="7" r="7" fill="#fff"/><path d="M5 4l3.5 3L5 10" stroke="#66287a" stroke-width="2" fill="none"/></svg></div>

  <div class="abs info" style="left:90px;top:3400px">
    <div class="ring"><svg width="24" height="24" viewBox="0 0 24 24"><path d="M6 2l4 4-2 3c1 3 4 6 7 7l3-2 4 4-3 4C10 21 3 14 2 5z" fill="#0a70b6"/></svg></div>
    <h5>PHONE</h5><p>(+316) 555 0142 7730</p>
  </div>
  <div class="abs info" style="left:315px;top:3400px">
    <div class="ring"><svg width="20" height="26" viewBox="0 0 20 26"><path d="M10 1C5 1 1 5 1 10c0 6 9 15 9 15s9-9 9-15c0-5-4-9-9-9z" fill="#0a70b6"/><circle cx="10" cy="10" r="3.5" fill="#fff"/></svg></div>
    <h5>HEAD OFFICE</h5><p>48 Harbor Lane Avenue, Westbrook,<br>North Region, PO 5510</p>
  </div>
  <div class="abs info" style="left:594px;top:3400px">
    <div class="ring fill"><svg width="20" height="26" viewBox="0 0 20 26"><path d="M10 1C5 1 1 5 1 10c0 6 9 15 9 15s9-9 9-15c0-5-4-9-9-9z" fill="#fff"/><circle cx="10" cy="10" r="3.5" fill="#0a70b6"/></svg></div>
    <h5>MAIN OFFICE</h5><p>72 Linden Park Road, Eastmoor,<br>Lake County, PO 6127</p>
  </div>
  <div class="abs info" style="left:843px;top:3400px">
    <div class="ring"><svg width="26" height="20" viewBox="0 0 26 20"><rect x="1" y="1" width="24" height="18" rx="2" fill="#0a70b6"/><path d="M2 3l11 8 11-8" stroke="#fff" stroke-width="2" fill="none"/></svg></div>
    <h5>EMAIL</h5><p>hello@lumaktrovenar.com</p>
  </div>

  <div class="abs foot-line" style="left:142px;width:360px"></div>
  <div class="abs foot-line" style="left:700px;width:358px"></div>
  <div class="abs social" style="left:507px"><i></i></div>
  <div class="abs social" style="left:555px"><i></i></div>
  <div class="abs social" style="left:603px"><i></i></div>
  <div class="abs social" style="left:651px"><i></i></div>

  <p class="abs copyright">Copyright © 2020 LumaKTrovenar . All rights reserved &nbsp;|&nbsp; Privacy Policy</p>
  <div class="abs bottom-bar"></div>
</div>
</body>
</html>
```